Business Card Design

I am the owner of a store (soon to open) that sells only handmade items such as pottery, textiles, blown glass, jewelry, etc. I need a card for customers to take with them, to handout to potential vendors/artists and to include in the bag of purchasers. So the card has to be a multi-tasker. My color scheme is ocre and eggplant. Visually I prefer patterns such as damask, toile, sweeping florals with a lot of curling vines, etc. I am not into modern, folk, cutesy and the like. My store has an upscale feel but doesn't take itself too seriously. I am kind of quirky and so are some of the items in my store.
Updates

Please read my brief before posting examples. I have received dozens of examples that have absolutely no resemblance to my brief. It is a waste of my time to have to eliminate and explain the reason for an elimination for cards that are totally off-base. It is a waste of your time as well. Thank you very much.

Target Market(s)

Upscale customers who appreciate the artistry and quality of handmade items.

Industry/Entity Type

Store

Contact Information for Business Card

FRONT:

Willowmere Atelier
3726 Brambleton Road, DD-4
Fernhollow, OH 19087
Phone: 215-554-0918
contact@willowmereatelier.com
www.willowmereatelier.com

BACK

Wondrously Handmade Treasures (centered)
Jewelry Textiles
Glass Candles
Pottery and more...

Font styles to use
Decorative
Script

Colors
7c59a5
fece3e

Requirements
Should not have
• Should not look like a corporate card. Should not look modern. Should not have colors that are not included in my description. Minor accents of other colors are OK, however, my primary color scheme must be prominent. I have indicated the other colors in my color preference. Dark reds, dark aquas and dark green. Should have a very feminine and stylistic font.

```html
<!DOCTYPE html>
<html lang="en">
<head>
<meta charset="utf-8">
<title>Willowmere Atelier – Business Card</title>
<link rel="stylesheet" href="https://fonts.googleapis.com/css2?family=Parisienne&family=Pinyon+Script&display=swap">
<style>
  :root {
    --backdrop: #ffffff;
    --eggplant: #5b2650;
    --eggplant-deep: #4a1d42;
    --lace-plum: #6a2f5e;
    --damask-violet: #7c59a5;
    --damask-rose: #b77bb0;
    --ochre: #fece3e;
    --ochre-deep: #d9a03a;
    --wood-ink: #4a2412;
    --cream: #f6ecd2;
    --lilac: #d9b6e2;
    --doily: #efe8dc;
    --doily-shade: #8a6a58;
  }
  * { box-sizing: border-box; margin: 0; padding: 0; }
  html, body { width: 1200px; height: 1000px; overflow: hidden; background: var(--backdrop); }
  .canvas { position: relative; width: 1200px; height: 1000px; }

  .card {
    position: absolute;
    width: 900px;
    height: 540px;
    overflow: hidden;
    box-shadow: 0 6px 18px rgba(0,0,0,0.35);
  }

  /* ---------- Back card ---------- */
  .card--back { left: 50px; top: 430px; background: var(--eggplant); }
  .back__doily-top {
    position: absolute; left: 0; top: 0; width: 360px; height: 170px;
    background: linear-gradient(135deg, var(--doily) 0%, var(--doily-shade) 70%, var(--doily) 100%);
    border-bottom-right-radius: 60% 90%;
  }
  .lace-band {
    position: absolute; left: 0; width: 100%; height: 46px;
    background: linear-gradient(180deg, var(--lace-plum), var(--eggplant-deep));
    border-top: 2px dotted rgba(217,160,58,0.5);
    border-bottom: 2px dotted rgba(217,160,58,0.5);
  }
  .back__lace-top { top: 168px; }
  .back__lace-bottom { top: 430px; left: 520px; width: 380px; }
  .back__doily-bottom {
    position: absolute; left: 0; top: 405px; width: 480px; height: 135px;
    background: radial-gradient(ellipse at 40% 80%, var(--doily-shade) 0%, var(--doily) 75%);
    border-top-right-radius: 70% 100%;
  }
  .back__tagline {
    position: absolute; left: 60px; top: 245px; width: 450px;
    font-family: "Pinyon Script", cursive;
    font-size: 52px; line-height: 66px; color: var(--lilac);
  }
  .back__tagline span { display: block; white-space: nowrap; }
  .back__tagline span + span { padding-left: 20px; }
  .back__offerings {
    position: absolute; left: 535px; top: 230px;
    font-family: "Pinyon Script", cursive;
    font-size: 50px; line-height: 64px; color: var(--cream);
    white-space: nowrap;
  }

  /* ---------- Front card ---------- */
  .card--front {
    left: 260px; top: 20px;
    background: linear-gradient(135deg, var(--damask-violet) 0%, var(--damask-rose) 35%, var(--ochre-deep) 55%, var(--damask-violet) 80%, var(--damask-rose) 100%);
  }
  .front__damask { position: absolute; inset: 0; }
  .front__plaque {
    position: absolute; left: 110px; top: 20px; width: 700px; height: 200px;
  }
  .front__lace {
    position: absolute; left: 0; top: 250px; width: 100%; height: 200px;
    background: linear-gradient(180deg, var(--lace-plum), var(--eggplant) 60%, var(--lace-plum));
    border-top: 3px dotted rgba(217,160,58,0.55);
    border-bottom: 3px dotted rgba(217,160,58,0.55);
  }
  .front__name {
    position: absolute; left: 110px; top: 52px; width: 700px; text-align: center;
    font-family: "Parisienne", cursive; font-size: 66px; color: var(--wood-ink);
    white-space: nowrap;
  }
  .front__web {
    position: absolute; left: 110px; top: 152px; width: 700px; text-align: center;
    font-family: "Parisienne", cursive; font-size: 26px; color: var(--cream);
  }
  .front__address {
    position: absolute; left: 70px; top: 265px;
    font-family: "Parisienne", cursive; font-size: 32px; line-height: 38px; color: var(--cream);
  }
  .front__contact {
    position: absolute; right: 60px; top: 335px; text-align: right;
    font-family: "Parisienne", cursive; font-size: 30px; line-height: 40px; color: var(--cream);
  }
</style>
</head>
<body>
<main class="canvas">

  <section class="card card--back" aria-label="Card back">
    <div class="back__doily-top" role="img" aria-label="Crocheted lace doily"></div>
    <div class="lace-band back__lace-top" role="img" aria-label="Eyelet lace trim band"></div>
    <p class="back__tagline"><span>Wondrously</span><span>Handmade Treasures</span></p>
    <div class="back__doily-bottom" role="img" aria-label="Crocheted lace doily"></div>
    <div class="lace-band back__lace-bottom" role="img" aria-label="Eyelet lace trim band"></div>
    <p class="back__offerings">Jewelry Textiles<br>Pottery Candles<br>Glass and more...</p>
  </section>

  <section class="card card--front" role="group" aria-label="Card front">
    <div class="front__damask" role="img" aria-label="Ochre and violet damask pattern background"></div>
    <div class="front__lace" role="img" aria-label="Eggplant eyelet lace band"></div>
    <svg class="front__plaque" viewBox="0 0 700 200" role="img" aria-label="Torn wooden plaque">
      <defs>
        <linearGradient id="woodGrain" x1="0" y1="0" x2="0" y2="1">
          <stop offset="0" stop-color="#a87548"/>
          <stop offset="0.5" stop-color="#8f6038"/>
          <stop offset="1" stop-color="#a06c40"/>
        </linearGradient>
      </defs>
      <path d="M10 110 L40 70 L90 40 L160 22 L260 12 L360 18 L450 10 L560 22 L620 40 L670 70 L692 105 L660 140 L600 165 L500 182 L380 190 L260 186 L150 176 L80 158 L30 135 Z"
            fill="url(#woodGrain)" stroke="#5e3a1c" stroke-width="3"/>
    </svg>
    <p class="front__name">Willowmere Atelier</p>
    <p class="front__web">www.willowmereatelier.com</p>
    <p class="front__address">3726 Brambleton Road, DD-4<br>Fernhollow, OH 19087</p>
    <p class="front__contact">Phone: 215-554-0918<br>contact@willowmereatelier.com</p>
  </section>

</main>
</body>
</html>
```